Business Cards for GPS Technology Business - Logo Supplied

Brelka Technologies Ltd. requires a business card design. Brelka is a startup GPS vehicle fleet tracking vendor. Our hardware/software helps business fleets be more productive and reduce operating costs. Our systems utilize a mix of GPS satellite, cell network and web technologies.
We would like to see a double sided original design utilizing our existing logo. Please use whatever colors will work with the blue logo.
As a business, we want to project the image of friendly and approachable lifetime business partners and advisors to our customers - “someone you can trust”. Words customers will use to describe us will include: knowledgeable, supportive, trustworthy and honest.
We will also require Viewtube, Chirpnet, Pagebook and Lookup+ backgrounds. Winner will be first in line to quote for this work (separate project).
Updates
Hello designers!
Target Market(s)
Target audience are working owners and managers of vehicle fleets. Usually male, age 30 to 60. Often have a trades background.
Industry/Entity Type
Business
Font styles to use
Requirements
Must have
- Please use the following dummy data for the design:
name: Ned Brelka
title: Director
address: 2389 Marlow Drive
city: Kelvaton, BC
postal code: K7P 2T4
cell phone number: 555-214-7730
business number: 555-309-4412
toll free number: 1-800-555-0199
web site address: www.brelka-example.com
tagline: GPS Fleet Tracking Specialists
Nice to have
- Abstract imagery relating to GPS tracking / fleet vehicles / technology
Should not have
- Do not use serif fonts.

```html
<!DOCTYPE html>
<html lang="en">
<head>
<meta charset="utf-8">
<title>Brelka Technologies Ltd. – Business Card</title>
<link href="https://fonts.googleapis.com/css2?family=Open+Sans:wght@400;700&display=swap" rel="stylesheet">
<style>
  :root {
    --brand-blue: #1f6cb9;
    --ink-blue: #1f6cb9;
    --text-grey: #666a6e;
    --title-grey: #4e5256;
    --card-white: #ffffff;
    --backdrop: #e6e6e4;
    --card-shadow: rgba(0, 0, 0, 0.18);
  }
  * { margin: 0; padding: 0; box-sizing: border-box; }
  html, body {
    width: 1200px;
    height: 800px;
    overflow: hidden;
    background: var(--backdrop);
    font-family: "Open Sans", Arial, sans-serif;
  }
  .canvas {
    position: relative;
    width: 1200px;
    height: 800px;
  }
  .card {
    position: absolute;
    top: 254px;
    width: 474px;
    height: 291px;
    border-radius: 16px;
    box-shadow: 0 4px 10px var(--card-shadow);
    overflow: hidden;
  }
  /* Front side */
  .card-front {
    left: 76px;
    background: var(--brand-blue);
    color: var(--card-white);
  }
  .card-front .wordmark {
    position: absolute;
    left: 37px;
    top: 168px;
    font-size: 52px;
    font-weight: 700;
    line-height: 1;
    letter-spacing: 1px;
  }
  .card-front .tagline {
    position: absolute;
    left: 37px;
    top: 238px;
    font-size: 15.5px;
    font-weight: 400;
  }
  /* Back side */
  .card-back {
    left: 656px;
    background: var(--card-white);
  }
  .card-back .person-name {
    position: absolute;
    left: 28px;
    top: 22px;
    font-size: 21px;
    font-weight: 400;
    color: var(--ink-blue);
  }
  .card-back .person-title {
    position: absolute;
    left: 28px;
    top: 52px;
    font-size: 16px;
    color: var(--title-grey);
  }
  .card-back .wordmark {
    position: absolute;
    right: 35px;
    top: 22px;
    font-size: 36px;
    font-weight: 700;
    line-height: 1;
    color: var(--ink-blue);
  }
  .contact-list {
    position: absolute;
    top: 176px;
    list-style: none;
  }
  .contact-list.address { left: 28px; }
  .contact-list.phones { left: 304px; }
  .contact-item {
    display: flex;
    align-items: center;
    height: 31px;
    font-size: 14.5px;
    color: var(--text-grey);
    white-space: nowrap;
  }
  .contact-icon {
    width: 16px;
    height: 16px;
    margin-right: 9px;
    flex-shrink: 0;
    fill: var(--ink-blue);
  }
</style>
</head>
<body>
<main class="canvas">

  <section class="card card-front" aria-label="Card front">
    <div class="wordmark">Brelka</div>
    <p class="tagline">GPS Fleet Tracking Specialists</p>
  </section>

  <section class="card card-back" aria-label="Card back">
    <h1 class="person-name">Ned Brelka</h1>
    <p class="person-title">Director</p>
    <div class="wordmark">Brelka</div>

    <ul class="contact-list address">
      <li class="contact-item">
        <svg class="contact-icon" viewBox="0 0 16 16" aria-hidden="true"><path d="M8 0.5a5.3 5.3 0 0 0-5.3 5.3C2.7 10 8 15.5 8 15.5s5.3-5.5 5.3-9.7A5.3 5.3 0 0 0 8 .5zm0 7.6a2.3 2.3 0 1 1 0-4.6 2.3 2.3 0 0 1 0 4.6z"/></svg>
        2389 Marlow Drive, Kelvaton
      </li>
      <li class="contact-item">
        <svg class="contact-icon" viewBox="0 0 16 16" aria-hidden="true"><path d="M1 3.5h14v1L8 9 1 4.5z"/><path d="M1 6l7 4.5L15 6v6.5H1z"/></svg>
        K7P 2T4
      </li>
      <li class="contact-item">
        <svg class="contact-icon" viewBox="0 0 16 16" aria-hidden="true"><path d="M8 1.5a6.5 6.5 0 1 0 0 13 6.5 6.5 0 0 0 0-13zm0 1.2c.8.7 1.5 2.1 1.7 3.8H6.3C6.5 4.8 7.2 3.4 8 2.7zM2.8 7.5h2.3c0 1.3.3 2.6.8 3.6a5.3 5.3 0 0 1-3.1-3.6zm0-1h.1a5.3 5.3 0 0 1 3-3.6c-.5 1-.8 2.3-.8 3.6zm5.2 6.8c-.8-.7-1.5-2.1-1.7-3.8h3.4c-.2 1.7-.9 3.1-1.7 3.8zm2.1-1.2c.5-1 .8-2.3.8-3.6h2.3a5.3 5.3 0 0 1-3.1 3.6zm.8-4.6c0-1.3-.3-2.6-.8-3.6a5.3 5.3 0 0 1 3.1 3.6z"/></svg>
        www.brelka-example.com
      </li>
    </ul>

    <ul class="contact-list phones">
      <li class="contact-item">
        <svg class="contact-icon" viewBox="0 0 16 16" aria-hidden="true"><path d="M1 5.5C1 3.5 4 2.5 8 2.5s7 1 7 3v1.5h-3.5V5.5h-7V7H1z"/><path d="M3.5 8.5 5.5 6h5l2 2.5V13h-9zM8 8.5a1.8 1.8 0 1 0 0 3.6 1.8 1.8 0 0 0 0-3.6z"/></svg>
        555-214-7730
      </li>
      <li class="contact-item">
        <svg class="contact-icon" viewBox="0 0 16 16" aria-hidden="true"><path d="M4.2 1.5 6 4.6 4.8 5.8c.8 1.9 2.4 3.5 4.3 4.3L10.3 9l3.1 1.8-.8 2.7c-5.6.3-10.4-4.6-10.1-10.2z"/><path d="M9.5 1.5a5 5 0 0 1 5 5h-1.2a3.8 3.8 0 0 0-3.8-3.8zm0 2.3a2.7 2.7 0 0 1 2.7 2.7H11a1.5 1.5 0 0 0-1.5-1.5z"/></svg>
        555-309-4412
      </li>
      <li class="contact-item">
        <svg class="contact-icon" viewBox="0 0 16 16" aria-hidden="true"><path d="M4 .5h8v15H4zm1.3 1.5v8h5.4V2zm.2 9.5v1.2h1.2v-1.2zm2 0v1.2h1.2v-1.2zm2 0v1.2h1.2v-1.2zm-4 2v1.2h1.2v-1.2zm2 0v1.2h1.2v-1.2zm2 0v1.2h1.2v-1.2z"/></svg>
        1-800-555-0199
      </li>
    </ul>
  </section>

</main>
</body>
</html>
```